Cloud Phone Service Brochure

We need a brochure for a Cloud Phone Service offering that we offer in Canada. We're a small company that cares about our client's success and protects their privacy. We would like to see designs that reflect us as a stable, trustworthy company which is also fast moving and leading edge. We see ourselves more like Quenby than Harn. Mosaic Vault has built our logo and business card, and we look forward to moving ahead here. I've attached our Business Card file so you have our logo as well as my own shot at some thoughts about content written as a trifold. That specific content does not need to be used, nor does it need to be a trifold. Those phone pictures are the actual phones we use.

```html
<!DOCTYPE html>
<html lang="en">
<head>
<meta charset="utf-8">
<title>Kudos — Cloud Phone Service</title>
<link rel="stylesheet" href="https://fonts.googleapis.com/css2?family=Open+Sans:wdth,wght@75,300;75,400&display=swap">
<style>
  :root {
    --page-navy: #1f436f;
    --kudos-blue: #2891d3;
    --copy-mist: #b3c2d7;
  }
  html, body {
    margin: 0;
    padding: 0;
    width: 960px;
    height: 1200px;
    overflow: hidden;
    background: var(--page-navy);
  }
  .page {
    position: relative;
    width: 960px;
    height: 1200px;
    overflow: hidden;
    background: var(--page-navy);
    font-family: "Open Sans", "Arial Narrow", sans-serif;
    font-stretch: 75%;
    font-weight: 300;
    color: var(--copy-mist);
  }
  .section-title {
    position: absolute;
    left: -71px;
    top: 1350px;
    width: 900px;
    margin: 0;
    transform: rotate(-90deg);
    transform-origin: 0 0;
    text-align: right;
    font-size: 390px;
    line-height: 1;
    font-weight: 300;
    letter-spacing: 2px;
    color: var(--kudos-blue);
    white-space: nowrap;
  }
  .lead-quote {
    position: absolute;
    left: 347px;
    top: 46px;
    width: 280px;
    margin: 0;
    font-size: 33px;
    line-height: 60px;
  }
  .testimonial {
    position: absolute;
    left: 633px;
    top: 443px;
    width: 280px;
    font-size: 28px;
    line-height: 48px;
  }
  .testimonial p {
    margin: 0 0 48px;
  }
</style>
</head>
<body>
  <main class="page">
    <h1 class="section-title">Kudos</h1>

    <p class="lead-quote">
      Boriam, tet di omni-<br>
      musamus aperaer<br>
      eptate precab il-<br>
      icimp oreritatur, vel<br>
      iur, to quatur aut<br>
      volorum faccabore<br>
      provid maximi, nim-<br>
      pos alit, sequi vo-<br>
      luptatur?
    </p>

    <div class="testimonial">
      <p>
        Boriam, tet di omni-<br>
        musamus aperaer<br>
        eptate precab ilicimp<br>
        oreritatur, vel iur, to<br>
        quatur aut volorum fac-<br>
        cabore provid maximi,<br>
        nimpos alit, sequi volup-<br>
        tatur?
      </p>
      <p>
        Suntor alita plistrum<br>
        ipsum fugias reribero to<br>
        maiore, eos maior sen-<br>
        totatiae. Nequis verum
      </p>
    </div>
  </main>
</body>
</html>
```